New Business Card Design For Re-Branded Company (New Logo)

We recently switched our DBA and had a new logo designed. We now need new business cards made around our new logo. We would like to stick with the color scheme in our logo: White, Orange, and Blue. We want to see original bold designs that reflect our position in the solar energy sector but we prefer simple over complicated.

We are curious about vertical designs so if you can translate your design onto a vertical layout we would be open to look at it. We especially like a few designs we have seen on here that are vertical with a black or very dark gray background. They have our logo on one side and then the normal vertical business card on the other side.

I have included a screenshot of one of the samples we like, labeled sample.jpg and a file we were given as an example of our logo on a dark background.

At the same time we are satisfied to stay with what we have always had in a horizontal format. If it's not a lot of extra work for you, designs that are submitted in both horizontal and vertical formats will be greatly appreciated.

Please submit your original, bold, clean designs for consideration. Contact us with any questions or comments that may arise.

Thank you and Good Luck,

RT

```html
<!DOCTYPE html>
<html lang="en">
<head>
<meta charset="utf-8">
<title>Radiant Tide – Vertical Business Card</title>
<link rel="stylesheet" href="https://fonts.googleapis.com/css2?family=Montserrat:wght@600&family=Source+Sans+3:wght@400;600&display=swap">
<style>
  :root {
    --backdrop: #6c7a94;
    --card-dark: #231f20;
    --card-blue: #1e75c0;
    --brand-blue: #2a7fd0;
    --brand-orange: #f07b26;
    --white: #ffffff;
  }
  html, body {
    margin: 0;
    padding: 0;
    width: 1200px;
    height: 900px;
    overflow: hidden;
    background: var(--backdrop);
  }
  .stage {
    position: relative;
    width: 1200px;
    height: 900px;
  }
  .card {
    position: absolute;
    top: 200px;
    width: 310px;
    height: 501px;
    box-sizing: border-box;
  }
  .card-front {
    left: 265px;
    background: var(--card-dark);
    border-radius: 50px 0 70px 0;
  }
  .card-back {
    left: 641px;
    background: var(--card-blue);
    border-radius: 0 50px 0 70px;
  }
  .brand-dot {
    position: absolute;
    left: 122px;
    top: 40px;
    width: 66px;
    height: 66px;
    border: 4px solid var(--brand-orange);
    border-radius: 50%;
    box-sizing: border-box;
  }
  .brand-name {
    position: absolute;
    left: 0;
    right: 0;
    top: 124px;
    margin: 0;
    text-align: center;
    font-family: "Montserrat", sans-serif;
    font-weight: 600;
    font-size: 35px;
    letter-spacing: -0.5px;
    color: var(--brand-blue);
    white-space: nowrap;
  }
  .contact {
    position: absolute;
    left: 27px;
    top: 327px;
    font-family: "Source Sans 3", sans-serif;
    color: var(--white);
    font-size: 14px;
    line-height: 16px;
  }
  .contact-name {
    margin: 0;
    font-weight: 600;
    font-size: 18px;
    line-height: 22px;
    color: var(--brand-blue);
  }
  .contact-role { margin: 2px 0 0; }
  .contact-address { margin: 18px 0 0; }
  .contact-line {
    margin: 10px 0 0;
    display: flex;
    align-items: center;
    gap: 6px;
  }
  .contact-line + .contact-line { margin-top: 4px; }
  .contact-line svg { width: 10px; height: 10px; fill: var(--brand-blue); }
  .back-name {
    position: absolute;
    left: 0;
    right: 0;
    top: 394px;
    margin: 0;
    text-align: center;
    font-family: "Montserrat", sans-serif;
    font-weight: 600;
    font-size: 35px;
    letter-spacing: -0.5px;
    color: var(--white);
    white-space: nowrap;
  }
</style>
</head>
<body>
<main class="stage">
  <section class="card card-front">
    <span class="brand-dot"></span>
    <h1 class="brand-name">RADIANT TIDE</h1>
    <div class="contact">
      <p class="contact-name">DANA WHITFIELD</p>
      <p class="contact-role">Managing Director</p>
      <p class="contact-address">1234, Address Goes Here<br>Country Name, 123456</p>
      <p class="contact-line">
        <svg viewBox="0 0 10 10" aria-hidden="true"><path d="M1 3.5C1 2 2.5 1.5 5 1.5S9 2 9 3.5L7.3 4.2 6.8 3H3.2L2.7 4.2Z M2 5h6l1 3.5H1Z"/></svg>
        <span>555-204-3187</span>
      </p>
      <p class="contact-line">
        <svg viewBox="0 0 10 10" aria-hidden="true"><path d="M0.5 2.5h9v5.5h-9Z M0.5 2.5 5 6 9.5 2.5" stroke="var(--card-dark)" stroke-width="0.8"/></svg>
        <span>hello@radianttide.com</span>
      </p>
    </div>
  </section>
  <section class="card card-back">
    <h2 class="back-name">RADIANT TIDE</h2>
  </section>
</main>
</body>
</html>
```